Online Trading Web-Design

Web design is required for a new startup that specialises in online trading between buyers and sellers of fashion apparel. The company is called: Bright Cove Hub (bch)

Website needs to be clean and css friendly. we like the idea of having a largish "banner" on the homepage which we can rotate using HTML5. examples of the banners are: http://au.plevrix.com/ ; http://www.dorvanqe.com.au/

the logo has been established already, please limit designs around the colors already established (see uploaded logo).
Updates

Hi, a few clarifications:

1. although the website deals in online trading for clothes etc. the main focus of the website needs to be about highlighting trading between buyers (clothing stores) and sellers (clothing brands). so the website wont be directly selling items of clothes etc.

Industry/Entity Type

Fashion

```html
<!DOCTYPE html>
<html lang="en">
<head>
<meta charset="utf-8">
<title>Bright Cove Hub — Fashion Catalog</title>
<link href="https://fonts.googleapis.com/css2?family=Arimo:ital,wght@0,400;0,700;1,400;1,700&family=Oswald:wght@400;500&display=swap" rel="stylesheet">
<style>
:root{
  --accent:#e4522a;
  --ink:#333;
  --muted:#777;
  --line:#dcdcdc;
  --page:#f3f3f3;
  --panel:#fff;
  --bar:#2e2e2e;
  --footer:#e7e7e7;
}
*{box-sizing:border-box;margin:0;padding:0}
html,body{width:1200px;height:2880px;overflow:hidden}
body{background:var(--page);font-family:"Arimo",Arial,sans-serif;color:var(--ink);font-size:15px;position:relative}
a{color:var(--accent);text-decoration:none}
.abs{position:absolute}
.photo{position:absolute;border-radius:2px}

/* top bar */
.top-bar{left:0;top:0;width:1200px;height:90px;background:var(--bar)}
.top-tools{right:40px;top:32px;display:flex;align-items:center;gap:12px;color:#eee;font-size:14px;white-space:nowrap}
.top-tools .field{height:28px;background:#fff;border:1px solid #999;color:#555;font-size:13px;padding:5px 8px}
.top-tools .search-btn{height:28px;background:#555;color:#fff;font-size:13px;padding:6px 10px}

/* navigation */
.main-nav{left:0;top:90px;width:1200px;height:80px;background:#fff;border-bottom:1px solid var(--line)}
.main-nav ul{list-style:none;display:flex;margin:20px 0 0 48px;gap:4px}
.main-nav li{font-size:15px;padding:13px 22px;color:#333;white-space:nowrap}
.main-nav li.active{background:var(--accent);color:#fff}

/* banner */
.banner{left:48px;top:196px;width:1112px;height:414px;background:linear-gradient(100deg,#c9c4c0 0%,#ebe8e5 35%,#f2f0ee 55%,#6a5e5c 80%,#2c2325 100%)}
.banner-caption{left:48px;top:450px;width:700px;height:160px;background:linear-gradient(90deg,rgba(0,0,0,.45),rgba(0,0,0,0))}
.banner-caption h2{font-family:"Oswald",sans-serif;font-weight:400;color:#fff;font-size:62px;margin:14px 0 0 40px;line-height:1}
.banner-caption p{color:#eee;font-size:14px;margin:8px 0 0 40px;width:520px;line-height:1.35}

/* left column */
.sidebar{left:48px;top:640px;width:350px}
.side-title{font-family:"Oswald",sans-serif;color:var(--accent);font-size:28px;font-weight:400;border-bottom:1px solid var(--line);padding-bottom:8px;margin-bottom:14px}
.cat-list{list-style:none;font-size:15px;line-height:30px;color:#555;margin-bottom:90px}
.cat-list .sub{padding-left:24px}
.cat-list .sub::before{content:"›  ";color:var(--accent)}
.news-item{margin-bottom:30px;border-bottom:1px solid var(--line);padding-bottom:14px}
.news-img{position:relative;height:112px;margin-bottom:14px}
.news-item h4{font-style:italic;font-size:17px;margin-bottom:8px}
.news-item p{font-size:13px;line-height:20px;color:var(--muted)}
.read-more{display:block;text-align:right;font-size:13px;margin-top:6px}
.promo{position:relative;height:300px;margin-bottom:18px;background:linear-gradient(135deg,#fff 0%,#fdf1ec 50%,#f3c2b2 100%)}
.promo-text{position:absolute;left:12px;top:40px;font-family:"Oswald",sans-serif;color:var(--accent);font-size:50px;line-height:1}
.promo-text small{font-family:"Arimo",sans-serif;font-size:15px;color:#555;font-style:italic;vertical-align:middle}
.promo-photo{position:absolute;right:20px;top:90px;width:170px;height:200px;background:linear-gradient(160deg,#f7c46a,#ea6fa5 55%,#8cc6e4);border-radius:2px}
.bullets{list-style:none;font-size:13px;line-height:20px;color:var(--muted);margin-top:6px}
.bullets li::before{content:"• ";color:var(--accent)}

/* main column */
.content{left:430px;top:640px;width:730px}
.crumb{font-size:13px;color:var(--muted);padding-bottom:10px;border-bottom:1px solid var(--line)}
.thumbs{display:flex;gap:12px;margin:18px 0}
.thumb{width:112px;height:140px;border:1px solid var(--line);background:#fff;padding:8px}
.thumb span{display:block;width:100%;height:100%}
.feature{position:relative;display:flex;gap:26px;border-top:1px solid var(--line);padding-top:18px;height:350px}
.feature-img{width:230px;height:300px;background:linear-gradient(180deg,#ecebee,#b9b8cc 50%,#d6d9e0)}
.feature-body h3{font-family:"Oswald",sans-serif;font-weight:400;color:var(--accent);font-size:36px;line-height:1}
.feature-body h4{font-size:22px;font-weight:700;margin:10px 0 12px}
.feature-body p{font-size:13px;line-height:20px;color:var(--muted);margin-bottom:10px;width:450px}
.pager-mini{position:absolute;right:0;bottom:6px;display:flex;gap:6px}
.pager-mini span{width:26px;height:26px;border:1px solid var(--line);font-size:13px;text-align:center;line-height:24px;background:#fff}
.pager-mini span.on{background:var(--accent);color:#fff;border-color:var(--accent)}
.catalog-title{font-family:"Oswald",sans-serif;font-weight:400;color:var(--accent);font-size:44px;margin:4px 0 18px;padding-bottom:10px;border-bottom:1px solid var(--line)}
.filters{background:#eee;border:1px solid var(--line);padding:14px 18px;font-size:13px;color:#555}
.filters .row{display:flex;gap:10px;align-items:center;margin-bottom:10px}
.filters .sel{background:#fff;border:1px solid #bbb;height:26px;padding:5px 8px;width:180px;white-space:nowrap}
.filters .btn{background:#666;color:#fff;padding:5px 12px}
.filters .order a{margin-left:12px;text-decoration:underline}
table{width:100%;border-collapse:collapse;margin-top:18px;font-size:13px}
th{background:#e4e4e4;color:#555;font-weight:400;text-align:left;height:32px;padding:0 10px}
td{border-bottom:1px solid var(--line);height:196px;padding:0 10px;vertical-align:middle}
td a{text-decoration:underline}
.prod-img{width:120px;height:170px;background:#fff;border:1px solid var(--line);padding:8px}
.prod-img span{display:block;width:100%;height:100%}
.price{font-weight:700;text-align:right;white-space:nowrap}
.pager{display:flex;justify-content:center;gap:12px;font-size:14px;margin-top:16px;color:#666}
.pager .on{color:#333;font-weight:700}

/* footer */
.footer{left:0;top:2430px;width:1200px;height:390px;background:var(--footer);border-top:1px solid #d0d0d0}
.footer-cols{display:flex;margin:40px 0 0 60px}
.footer-col{width:270px;padding-right:20px}
.footer-col h5{font-style:italic;font-size:18px;margin-bottom:14px}
.footer-col ul{list-style:none;font-size:13px;line-height:22px}
.footer-col li::before{content:"■ ";color:var(--accent);font-size:9px}
.footer-col li a{text-decoration:underline}
.social{display:flex;align-items:center;gap:14px;margin-bottom:26px;font-size:13px;color:#555}
.social i{display:block;width:58px;height:58px;background:#6f6f6f;border-radius:6px}
.contact{font-size:13px;line-height:20px;color:#555}
.bottom-bar{left:0;top:2820px;width:1200px;height:60px;background:var(--bar);color:#aaa;font-size:13px;padding:22px 60px}
</style>
</head>
<body>

<header class="abs top-bar">
  <div class="abs top-tools">
    <span>Choose a Producer</span><span class="field">Choose a Producer ▾</span>
    <span>Search for Product</span><span class="field" style="width:140px"></span><span class="search-btn">Search</span>
  </div>
</header>

<nav class="abs main-nav">
  <ul>
    <li class="active">Home</li><li>Template Features</li><li>Catalog Manager</li><li>Submenu</li><li>The Portalis Project</li><li>The Portalis Community</li><li>RTL Languages</li>
  </ul>
</nav>

<div class="photo banner" role="img" aria-label="Banner photo of a clothing boutique with garments on rails and a mannequin"></div>
<div class="abs banner-caption">
  <h2>Collection 2012</h2>
  <p>Fresh seasonal lines from leading brands, now open for trade between stores and labels across the network.</p>
</div>

<aside class="abs sidebar">
  <h3 class="side-title">Choose a Category</h3>
  <ul class="cat-list">
    <li>Fashion Zone For Men</li><li class="sub">T-Shirts</li><li class="sub">Hoodies</li><li class="sub">Jeans</li>
    <li>Fashion Zone For Women</li><li class="sub">Tops</li><li class="sub">Sweaters</li><li class="sub">Jeans</li>
  </ul>

  <h3 class="side-title">Latest News</h3>
  <div class="news-item">
    <div class="photo news-img" style="width:350px;background:linear-gradient(90deg,#f6d0df,#e783ab 60%,#f4c3d4)" role="img" aria-label="Fashion magazine photo in pink tones"></div>
    <h4>Vesta Fashion Magazine</h4>
    <p>Pellentesque consectetur quis dolor tempus aliquam. Nunc nec neque, pharetra ac vestibulum ut, facilisis sit amet, rhoncus sit amet.</p>
    <a class="read-more">Read more...</a>
  </div>
  <div class="news-item">
    <div class="photo news-img" style="width:350px;height:96px;background:linear-gradient(90deg,#ececec,#8a827a 50%,#ececec)" role="img" aria-label="Photo of men wearing outerwear"></div>
    <h4>New Outerwear Collection</h4>
    <p>Pellentesque consectetur quis dolor tempus aliquam. Nunc nec neque, pharetra ac vestibulum ut, facilisis sit amet.</p>
    <a class="read-more">Read more...</a>
  </div>
  <div class="news-item">
    <div class="photo news-img" style="width:350px;height:96px;background:linear-gradient(90deg,#e8e8e8,#c9a4a0 30%,#9fb7d6 70%,#e8e8e8)" role="img" aria-label="Photo of colourful vintage sneakers"></div>
    <h4>Strider Vintage Sneakers</h4>
    <p>Pellentesque consectetur quis dolor tempus aliquam. Nunc nec neque, pharetra ac vestibulum ut.</p>
    <a class="read-more">Read more...</a>
  </div>
  <div class="promo">
    <div class="promo-text">30% <small>off after your first purchase*</small></div>
    <div class="promo-photo" role="img" aria-label="Photo of a shopper carrying colourful bags"></div>
  </div>
  <h4 style="font-style:italic;font-size:17px;margin-bottom:8px">Get Discounts</h4>
  <p style="font-size:13px;line-height:20px;color:var(--muted)">Quisque sed mi lorem, nec posuere purus. Fusce cursus varius nisl, tempus dapibus ligula imperdiet.</p>
  <ul class="bullets"><li>Curabitur sed porta</li><li>Nunc et lorem turpis</li><li>Donec interdum arcu</li></ul>
  <a class="read-more">Read more...</a>
</aside>

<main class="abs content">
  <div class="crumb">You are here: &nbsp;<a>Home</a></div>
  <div class="thumbs">
    <div class="thumb"><span style="background:linear-gradient(#d8d8e4,#6f6e95)" role="img" aria-label="Product photo: navy sweater"></span></div>
    <div class="thumb"><span style="background:linear-gradient(#dcdcdc,#8a8a8a)" role="img" aria-label="Product photo: grey jacket"></span></div>
    <div class="thumb"><span style="background:linear-gradient(#d6d6d6,#6e6e6e)" role="img" aria-label="Product photo: dark hoodie"></span></div>
    <div class="thumb"><span style="background:linear-gradient(#e2e2e2,#9a9a9a)" role="img" aria-label="Product photo: grey top"></span></div>
    <div class="thumb"><span style="background:linear-gradient(#ecebe9,#b8b1ab)" role="img" aria-label="Product photo: beige sweater"></span></div>
    <div class="thumb"><span style="background:linear-gradient(#e4e3ec,#76759c)" role="img" aria-label="Product photo: navy top"></span></div>
  </div>
  <div class="feature">
    <div class="feature-img" role="img" aria-label="Product photo: asymmetrical gathered tee with denim shorts"></div>
    <div class="feature-body">
      <h3>Sweaters</h3>
      <h4>Asymmetrical Gathered Tee</h4>
      <p>Lorem ipsum dolor sit amet, consectetur adipiscing elit. Proin hendrerit vehicula odio, non porta lacus faucibus sed. Donec faucibus purus ante, nec imperdiet lorem.</p>
      <p>Quisque quam tortor, consequat ut tellus feugiat, porta nulla. Integer mollis varius nisi, quis pharetra urna vel lacus imperdiet malesuada. Nullam posuere enim sed lorem auctor.</p>
      <p>Mauris diam arcu odio.</p>
      <a style="font-size:13px">» More...</a>
    </div>
    <div class="pager-mini"><span class="on">1</span><span>2</span></div>
  </div>

  <h2 class="catalog-title">Welcome to the Fashion Catalog</h2>
  <div class="filters">
    <div class="row">Filters <span class="sel">– Choose Category – ▾</span><span class="sel">– Choose Manufacturer – ▾</span></div>
    <div class="row">Search <span class="sel" style="width:200px"></span><span class="btn">Go</span><span class="btn">Reset</span></div>
    <div class="order">Order: <a>Name</a><a>Category</a><a>Manufacturer</a><a>Price</a><a>Date</a></div>
  </div>
  <table>
    <thead><tr><th></th><th>Name</th><th>Description</th><th>Category</th><th>Producer</th><th style="text-align:right">Price</th></tr></thead>
    <tbody>
      <tr><td><div class="prod-img"><span style="background:linear-gradient(#e6e5ee,#7b7aa0)" role="img" aria-label="Product photo: navy gathered tee"></span></div></td><td><a>Asymmetrical Gathered Tee</a></td><td>Soft jersey top</td><td><a>Sweaters</a></td><td><a>Harbor</a></td><td class="price">44,50 €</td></tr>
      <tr><td><div class="prod-img"><span style="background:linear-gradient(#e4e4e4,#555)" role="img" aria-label="Product photo: black jeans"></span></div></td><td><a>Black Jeans</a></td><td>Slim fit denim</td><td><a>Jeans</a></td><td><a>Linden</a></td><td class="price">29,00 €</td></tr>
      <tr><td><div class="prod-img"><span style="background:linear-gradient(#eeeeee,#a7a7b0)" role="img" aria-label="Product photo: crane panel top"></span></div></td><td><a>Crane Panel Top</a></td><td>Light cotton top</td><td><a>Tops</a></td><td><a>Linden</a></td><td class="price">19,90 €</td></tr>
      <tr><td><div class="prod-img"><span style="background:linear-gradient(#ededed,#5a5a66)" role="img" aria-label="Product photo: high-rise skinny jeans"></span></div></td><td><a>High-Rise Skinny Jeans</a></td><td>Stretch denim</td><td><a>Jeans</a></td><td><a>Harbor</a></td><td class="price">29,90 €</td></tr>
    </tbody>
  </table>
  <div class="pager"><span>Start</span><span>Prev</span><span class="on">1</span><a>2</a><a>3</a><a>Next</a><a>End</a></div>
</main>

<footer class="abs footer">
  <div class="footer-cols">
    <div class="footer-col"><h5>Latest Articles</h5><ul><li><a>Beginners</a></li><li><a>Getting Help</a></li><li><a>Getting Started</a></li><li><a>Portalis</a></li><li><a>Parameters</a></li><li><a>Professionals</a></li></ul></div>
    <div class="footer-col"><h5>Popular Articles</h5><ul><li><a>Template Features</a></li><li><a>The Portalis Project</a></li><li><a>Catalog Manager</a></li><li><a>Module Positions</a></li><li><a>The Portalis Community</a></li><li><a>Template Parameters</a></li></ul></div>
    <div class="footer-col"><h5>Follow Us</h5>
      <div class="social"><i></i>Find us on Friendwall</div>
      <div class="social"><i></i>Find us on Chirper</div>
    </div>
    <div class="footer-col"><h5>Contact Us</h5>
      <p class="contact">Bright Cove Hub Catalog<br>Kestrel Lane 41<br>00-000 Harbour Town<br>Tel: 000 000 000<br>Fax: 000 000 001<br>E-mail: <a style="text-decoration:underline">hello@brightcovehub.example</a></p>
    </div>
  </div>
</footer>
<div class="abs bottom-bar">2013 All Rights Reserved</div>

</body>
</html>
```